Letter Head Design

I need a letter head design based on my company logo that I attached.
Include phone number: (403)582-3140
Address: 417 Brindlewood Avenue NE, Calgary, Alberta, Canada, T3M 4K8

Industry/Entity Type

It Company

```html
<!DOCTYPE html>
<html lang="en">
<head>
<meta charset="utf-8">
<title>BrightNook Interiors Corp. – Letterhead</title>
<link href="https://fonts.googleapis.com/css2?family=Roboto:wght@400;500&family=Montserrat:wght@500;700&display=swap" rel="stylesheet">
<style>
  :root {
    --backdrop: #e2e2e2;
    --paper: #fbfbfb;
    --brand-blue: #2f5fae;
    --brand-sky: #2a7cc4;
    --brand-green: #6dbb3a;
    --ink: #3a3a3a;
    --white: #ffffff;
  }
  * { margin: 0; padding: 0; box-sizing: border-box; }
  html, body {
    width: 942px;
    height: 1200px;
    overflow: hidden;
    background: var(--backdrop);
  }
  .letterhead {
    position: absolute;
    left: 45px;
    top: 0;
    width: 852px;
    height: 1200px;
    background: var(--paper);
    overflow: hidden;
  }
  .masthead {
    position: absolute;
    top: 53px;
    left: 0;
    width: 100%;
    display: flex;
    flex-direction: column;
    align-items: center;
  }
  .masthead-square {
    width: 104px;
    height: 104px;
    background: var(--brand-green);
    border-radius: 4px;
  }
  .masthead-name {
    margin-top: 14px;
    font-family: "Roboto", sans-serif;
    font-weight: 400;
    font-size: 34px;
    line-height: 1;
    color: var(--brand-sky);
  }
  .contact {
    position: absolute;
    left: 75px;
    top: 1143px;
    font-family: "Montserrat", sans-serif;
    font-weight: 500;
    font-size: 9.5px;
    letter-spacing: 0.3px;
    color: var(--ink);
    text-transform: uppercase;
    line-height: 15px;
  }
  .contact-label {
    font-weight: 700;
    color: var(--brand-blue);
  }
  .footer-band {
    position: absolute;
    left: 0;
    bottom: 0;
    width: 600px;
    height: 14px;
    background: var(--brand-green);
  }
  .footer-block {
    position: absolute;
    right: 0;
    bottom: 0;
    width: 290px;
    height: 64px;
    background: var(--brand-blue);
    clip-path: polygon(58px 0, 100% 0, 100% 100%, 0 100%);
    display: flex;
    align-items: center;
    padding-left: 76px;
    gap: 12px;
  }
  .footer-square {
    width: 38px;
    height: 38px;
    border: 2px solid var(--white);
    border-radius: 3px;
  }
  .footer-name {
    font-family: "Roboto", sans-serif;
    font-weight: 400;
    font-size: 22px;
    color: var(--white);
  }
</style>
</head>
<body>
  <main class="letterhead">
    <header class="masthead">
      <div class="masthead-square" aria-hidden="true"></div>
      <div class="masthead-name">BrightNook</div>
    </header>

    <address class="contact" style="font-style: normal;">
      <div><span class="contact-label">Phon.</span> (403) 582-3140</div>
      <div><span class="contact-label">Office.</span> 417 Brindlewood Avenue NE, Calgary, Alberta, Canada, T3M 4K8</div>
    </address>

    <div class="footer-band" aria-hidden="true"></div>
    <footer class="footer-block">
      <div class="footer-square" aria-hidden="true"></div>
      <div class="footer-name">BrightNook</div>
    </footer>
  </main>
</body>
</html>
```